Beer Can Label design - HAZY NEIPA

Hazy NEIPA. (Acronym for New England India Pale Ale)
Full sleeve (473ml)
5.00" x 8.125" Inches
Write up on can reverse.
Opaque haze in appearance derived from specific oats, wheat, and water chemistry. This brew bolsters a dense and creamy head, leaving behind a soft and silky mouth-feel. Expect an intense tropical fruit centric aroma and flavour. Our timely hop additions contributes to less bitterness than typical IPA’s.
Logo is to be on front, towards bottom. Title near top.
Looking for something that stands out. Bold.
Target Market(s)
Craft beer enthusiasts
Industry/Entity Type
Beer & Brewing
Requirements
Must have
- Eye catching.

```html
<!DOCTYPE html>
<html lang="en">
<head>
<meta charset="utf-8">
<title>Hazy NEIPA – Can Label</title>
<link href="https://fonts.googleapis.com/css2?family=Smokum&family=Oswald:wght@500&family=Archivo+Black&display=swap" rel="stylesheet">
<style>
  :root {
    --backdrop: #757575;
    --amber-light: #d9982e;
    --amber: #c47a1f;
    --amber-deep: #a85a16;
    --ink: #1a1a1a;
    --cream: #ffffff;
    --skyline: rgba(150, 85, 20, 0.32);
  }
  * { box-sizing: border-box; margin: 0; padding: 0; }
  html, body {
    width: 1048px; height: 1200px; overflow: hidden;
    background: var(--backdrop);
  }
  .label {
    position: absolute; left: 183px; top: 25px;
    width: 682px; height: 1150px;
    background: var(--cream);
    overflow: hidden;
  }
  .top-band {
    position: absolute; left: 0; top: 0; width: 100%; height: 52px;
    background: var(--ink); color: var(--cream);
    display: flex; align-items: center; justify-content: center; gap: 30px;
    font-family: "Oswald", sans-serif; font-weight: 500;
    font-size: 17px; letter-spacing: 3px; white-space: nowrap;
  }
  .top-band .dot {
    width: 16px; height: 16px; border-radius: 50%; background: var(--cream);
  }
  .amber-field {
    position: absolute; left: 0; top: 52px; width: 100%; height: 798px;
    background: radial-gradient(ellipse at 60% 20%, var(--amber-light) 0%, var(--amber) 55%, var(--amber-deep) 100%);
  }
  .skyline-area {
    position: absolute; left: 0; bottom: 0; width: 100%; height: 320px;
    background: linear-gradient(to bottom, rgba(0,0,0,0) 0%, var(--skyline) 35%, var(--skyline) 100%);
  }
  .divider {
    position: absolute; left: 0; top: 850px; width: 100%; height: 15px;
    background: var(--ink);
  }
  .title {
    position: absolute; left: 0; top: 0; width: 682px; height: 620px;
    font-family: "Smokum", serif;
  }
  .title .shade { fill: var(--cream); }
  .title .face { fill: var(--ink); }
  .tagline {
    position: absolute; left: 0; top: 603px; width: 100%;
    display: flex; align-items: center; justify-content: center; gap: 8px;
    font-family: "Oswald", sans-serif; font-weight: 500;
    font-size: 26px; letter-spacing: 10px; color: var(--ink); white-space: nowrap;
  }
  .tagline .rule { width: 36px; height: 2px; background: var(--ink); }
  .brand {
    position: absolute; left: 0; top: 920px; width: 100%;
    display: flex; align-items: center; justify-content: center; gap: 16px;
    font-family: "Oswald", sans-serif; font-weight: 500;
    font-size: 40px; letter-spacing: 2px; color: var(--ink); white-space: nowrap;
  }
  .brand .mark {
    width: 30px; height: 30px; border-radius: 50%; background: var(--ink);
  }
  .volume {
    position: absolute; left: 0; top: 1095px; width: 100%; text-align: center;
    font-family: "Archivo Black", sans-serif; font-size: 28px;
    letter-spacing: 1px; color: var(--ink);
  }
</style>
</head>
<body>
  <main class="label">
    <div class="top-band">
      <span>AMET</span><span class="dot"></span>
      <span>LOREM IPSUM DOLOR SIT AMET</span><span class="dot"></span>
      <span>LOREM</span>
    </div>
    <div class="amber-field">
      <div class="skyline-area" role="img" aria-label="Faint industrial city skyline silhouette"></div>
    </div>
    <div class="divider"></div>
    <svg class="title" viewBox="0 0 682 620" role="img" aria-label="Hazy NEIPA">
      <text class="shade" x="345" y="353" text-anchor="middle" font-size="235" textLength="330" lengthAdjust="spacingAndGlyphs">HAZY</text>
      <text class="face" x="341" y="350" text-anchor="middle" font-size="235" textLength="330" lengthAdjust="spacingAndGlyphs">HAZY</text>
      <text class="shade" x="345" y="588" text-anchor="middle" font-size="300" textLength="520" lengthAdjust="spacingAndGlyphs">NEIPA</text>
      <text class="face" x="341" y="585" text-anchor="middle" font-size="300" textLength="520" lengthAdjust="spacingAndGlyphs">NEIPA</text>
    </svg>
    <p class="tagline"><span class="rule"></span>FOR THE HOP HEADS!<span class="rule"></span></p>
    <div class="brand"><span class="mark"></span>FOUNDRY ROW BREW HOUSE</div>
    <p class="volume">473ML</p>
  </main>
</body>
</html>
```